Need wine label for brand that is named: Tolmesha Vineyards & Winery

Tolmesha is a yoga way of breathing. In Sanskrit Tolmesha means "flying up." I would like a creative wine label that articulates Tolmesha. The label should include a graphic and the name Tolmesha on one line and Vineyards & Winery in smaller print underneath Tolmesha.

```html
<!DOCTYPE html>
<html lang="en">
<head>
<meta charset="utf-8">
<title>Tolmesha Vineyards &amp; Winery — Wine Label</title>
<link href="https://fonts.googleapis.com/css2?family=Josefin+Sans:wght@300;400&display=swap" rel="stylesheet">
<style>
  :root {
    --page: #ffffff;
    --frame-pink: #ff14a5;
    --panel-magenta: #c4108a;
    --band-magenta: #bd0f83;
    --cloud-light: #f7c4e6;
    --cloud-mid: #e070bd;
    --ink-white: #ffffff;
    --ink-blush: #f7a3d8;
  }
  html, body {
    margin: 0;
    padding: 0;
    width: 770px;
    height: 1200px;
    overflow: hidden;
    background: var(--page);
  }
  .label {
    display: block;
    width: 770px;
    height: 1200px;
  }
  .label__frame { fill: var(--frame-pink); }
  .label__panel { fill: var(--panel-magenta); }
  .label__band { fill: var(--band-magenta); }
  .label__diamond { fill: var(--ink-white); }
  .label__rule { stroke: var(--ink-white); stroke-width: 2; }
  .label__name {
    font-family: "Josefin Sans", sans-serif;
    font-weight: 300;
    font-size: 41px;
    letter-spacing: 3px;
    fill: var(--ink-white);
  }
  .label__subtitle {
    font-family: "Josefin Sans", sans-serif;
    font-weight: 300;
    font-size: 17.5px;
    letter-spacing: 1.2px;
    fill: var(--ink-blush);
  }
</style>
</head>
<body>
<svg class="label" viewBox="0 0 500 780" preserveAspectRatio="none" xmlns="http://www.w3.org/2000/svg">
  <defs>
    <clipPath id="panel-shape">
      <path d="M250,70 C262,120 300,150 335,160 L335,195 C380,205 405,240 405,290 L405,705 L95,705 L95,290 C95,240 120,205 165,195 L165,160 C200,150 238,120 250,70 Z"/>
    </clipPath>
    <radialGradient id="sky-upper" cx="50%" cy="55%" r="65%">
      <stop offset="0%" stop-color="var(--panel-magenta)"/>
      <stop offset="45%" stop-color="var(--cloud-mid)"/>
      <stop offset="100%" stop-color="var(--cloud-light)"/>
    </radialGradient>
    <radialGradient id="sky-lower" cx="50%" cy="40%" r="70%">
      <stop offset="0%" stop-color="var(--cloud-mid)"/>
      <stop offset="55%" stop-color="var(--cloud-light)"/>
      <stop offset="100%" stop-color="var(--cloud-mid)"/>
    </radialGradient>
  </defs>

  <path class="label__frame" d="M250,18 C262,62 300,112 350,130 L350,170 C420,186 452,232 452,292 L452,748 L48,748 L48,292 C48,232 80,186 150,170 L150,130 C200,112 238,62 250,18 Z"/>

  <path class="label__panel" d="M250,70 C262,120 300,150 335,160 L335,195 C380,205 405,240 405,290 L405,705 L95,705 L95,290 C95,240 120,205 165,195 L165,160 C200,150 238,120 250,70 Z"/>

  <g clip-path="url(#panel-shape)">
    <rect role="img" aria-label="Mirrored pink cloudscape rising into the sky" x="95" y="232" width="310" height="150" fill="url(#sky-upper)"/>
    <rect class="label__band" x="95" y="382" width="310" height="110"/>
    <rect role="img" aria-label="Mirrored pink clouds lifting upward" x="95" y="492" width="310" height="210" fill="url(#sky-lower)"/>
  </g>

  <rect class="label__diamond" x="244" y="59" width="12" height="12" transform="rotate(45 250 65)"/>

  <g class="label__diamonds label__diamonds--left">
    <rect class="label__diamond" x="62" y="524" width="12" height="12" transform="rotate(45 68 530)"/>
    <rect class="label__diamond" x="62" y="558" width="12" height="12" transform="rotate(45 68 564)"/>
    <rect class="label__diamond" x="62" y="591" width="12" height="12" transform="rotate(45 68 597)"/>
    <rect class="label__diamond" x="62" y="624" width="12" height="12" transform="rotate(45 68 630)"/>
    <rect class="label__diamond" x="62" y="657" width="12" height="12" transform="rotate(45 68 663)"/>
  </g>
  <g class="label__diamonds label__diamonds--right">
    <rect class="label__diamond" x="424" y="524" width="12" height="12" transform="rotate(45 430 530)"/>
    <rect class="label__diamond" x="424" y="558" width="12" height="12" transform="rotate(45 430 564)"/>
    <rect class="label__diamond" x="424" y="591" width="12" height="12" transform="rotate(45 430 597)"/>
    <rect class="label__diamond" x="424" y="624" width="12" height="12" transform="rotate(45 430 630)"/>
    <rect class="label__diamond" x="424" y="657" width="12" height="12" transform="rotate(45 430 663)"/>
  </g>
  <g class="label__diamonds label__diamonds--base">
    <rect class="label__diamond" x="179" y="718" width="12" height="12" transform="rotate(45 185 724)"/>
    <rect class="label__diamond" x="212" y="718" width="12" height="12" transform="rotate(45 218 724)"/>
    <rect class="label__diamond" x="244" y="718" width="12" height="12" transform="rotate(45 250 724)"/>
    <rect class="label__diamond" x="277" y="718" width="12" height="12" transform="rotate(45 283 724)"/>
    <rect class="label__diamond" x="310" y="718" width="12" height="12" transform="rotate(45 316 724)"/>
  </g>

  <line class="label__rule" x1="117" y1="393" x2="381" y2="393"/>
  <text class="label__name" x="250" y="438" text-anchor="middle">TOLMESHA</text>
  <text class="label__subtitle" x="250" y="474" text-anchor="middle">VINEYARDS &amp; WINERY</text>
</svg>
</body>
</html>
```